Podcast Cover Art for Fast Growing Show (Ill include a gracious tip!)

This artwork is for "The Steadfast Fellow Show." The podcast is for men, and it's all about self-improvement, confidence, success, money, women and masculinity. It's for the guy who wants to improve himself. I'd like for my picture to be included — in black and white — and I want the text to read: "The Steadfast Fellow Show" and somewhere in there it'll say: "with Dale Prowen." I'm open to color schemes. The podcast is a little edgy so I'd like for that to be represented in the design. Thank you! (((Here's the podcast page if you wanna check it out: http://steadfastfellowshow.castorbit.net/)))

Target Market(s)

Men who want to attract women and improve their lives!

Font styles to use
Serif

Colors

Designer to choose colors to be used in the design.

Requirements
Must have
• My image in it (in black and white) and the two titles: "The Steadfast Fellow Show" and "with Dale Prowen"
Nice to have
• My logo in it somehow (which is the arrow looking logo attached below). I've also found that my image looks best in black and white and with a circular type cut out (although I'm open to different design ideas). I've attached my logo with a circular cut out below so you can see what I'm talking about.
Should not have
• Flowers. Teddy bears. ice cream.

```html
<!DOCTYPE html>
<html lang="en">
<head>
<meta charset="utf-8">
<title>The Steadfast Fellow Show – Cover Art</title>
<link rel="stylesheet" href="https://fonts.googleapis.com/css2?family=PT+Serif:wght@400;700&display=swap">
<style>
  :root {
    --paper: #fbfaf8;
    --ink: #141414;
    --band-red: #f01a0a;
    --band-red-dark: #c40f0a;
    --orange: #f2641c;
    --amber: #f7b42c;
    --crimson: #d41e1e;
    --violet: #a64bd6;
    --lavender: #c9b7f2;
    --royal: #2a52e0;
    --sky: #7fb6ee;
    --navy: #1f3a64;
    --slate: #5e7f9a;
    --white: #ffffff;
  }
  html, body {
    margin: 0;
    padding: 0;
    width: 1200px;
    height: 1200px;
    overflow: hidden;
    background: var(--paper);
  }
  .cover {
    position: relative;
    width: 1200px;
    height: 1200px;
    overflow: hidden;
    background: var(--paper);
    font-family: "PT Serif", Georgia, serif;
  }
  .cover__stripes {
    position: absolute;
    inset: 0;
  }
  .cover__portrait {
    position: absolute;
    left: 108px;
    top: 52px;
    width: 984px;
    height: 984px;
    border-radius: 50%;
    overflow: hidden;
    background: var(--white);
  }
  .cover__portrait-photo {
    position: absolute;
    left: 0;
    right: 0;
    top: 90px;
    bottom: 0;
    background:
      radial-gradient(ellipse 42% 38% at 50% 46%, #b9b9b9 0%, #8c8c8c 55%, rgba(140,140,140,0) 100%),
      linear-gradient(180deg, rgba(255,255,255,0) 0%, rgba(255,255,255,0) 62%, #2e2e2e 78%, #1c1c1c 100%);
  }
  .cover__brand {
    position: absolute;
    right: 48px;
    top: 56px;
    display: flex;
    align-items: center;
    gap: 10px;
    color: var(--ink);
    font-size: 22px;
    font-weight: 700;
    letter-spacing: 2px;
  }
  .cover__brand-square {
    width: 18px;
    height: 18px;
    background: var(--ink);
  }
  .cover__title-band {
    position: absolute;
    left: 0;
    right: 0;
    top: 1002px;
    height: 110px;
    background: linear-gradient(90deg, var(--band-red) 0%, var(--band-red) 60%, var(--band-red-dark) 100%);
    display: flex;
    align-items: center;
    justify-content: center;
  }
  .cover__title {
    margin: 0;
    color: var(--white);
    font-size: 64px;
    font-weight: 400;
    letter-spacing: 1px;
    line-height: 1;
  }
  .cover__host {
    position: absolute;
    left: 0;
    right: 0;
    top: 1128px;
    text-align: center;
    color: var(--ink);
    font-size: 31px;
    font-weight: 700;
    letter-spacing: 5px;
    text-transform: uppercase;
  }
</style>
</head>
<body>
<main class="cover">
  <svg class="cover__stripes" width="1200" height="1200" viewBox="0 0 1200 1200" aria-hidden="true">
    <g transform="rotate(32 600 600)">
      <rect x="-400" y="-330" width="2000" height="70" fill="var(--lavender)" opacity="0.7"/>
      <rect x="-400" y="-260" width="2000" height="60" fill="var(--amber)"/>
      <rect x="-400" y="-200" width="2000" height="70" fill="var(--orange)"/>
      <rect x="-400" y="-130" width="2000" height="50" fill="var(--crimson)"/>
      <rect x="-400" y="-80" width="2000" height="55" fill="var(--violet)" opacity="0.85"/>
      <rect x="-400" y="0" width="2000" height="70" fill="var(--sky)" opacity="0.7"/>
      <rect x="-400" y="70" width="2000" height="90" fill="var(--royal)"/>
      <rect x="-400" y="160" width="2000" height="60" fill="var(--sky)" opacity="0.6"/>
      <rect x="-400" y="440" width="2000" height="50" fill="var(--amber)" opacity="0.8"/>
      <rect x="-400" y="490" width="2000" height="60" fill="var(--orange)"/>
      <rect x="-400" y="900" width="2000" height="60" fill="var(--amber)"/>
      <rect x="-400" y="960" width="2000" height="70" fill="var(--orange)"/>
      <rect x="-400" y="1030" width="2000" height="40" fill="var(--crimson)"/>
      <rect x="-400" y="1100" width="2000" height="80" fill="var(--slate)" opacity="0.7"/>
      <rect x="-400" y="1180" width="2000" height="120" fill="var(--navy)"/>
    </g>
    <circle cx="24" cy="790" r="80" fill="none" stroke="var(--white)" stroke-width="14" opacity="0.6"/>
    <circle cx="1100" cy="790" r="60" fill="none" stroke="var(--white)" stroke-width="12" opacity="0.5"/>
  </svg>

  <div class="cover__portrait">
    <div class="cover__portrait-photo" role="img" aria-label="Black and white portrait of the host, hands steepled in front of his chin"></div>
  </div>

  <div class="cover__brand">
    <span class="cover__brand-square"></span>
    <span class="cover__brand-name">STEADFAST</span>
  </div>

  <div class="cover__title-band">
    <h1 class="cover__title">The Steadfast Fellow Show</h1>
  </div>

  <p class="cover__host">Dale Prowen</p>
</main>
</body>
</html>
```